Sign Front of Business

Sign for front of workshop. We want KRT Mechanical in same font and colour as logo then the logo after name. Would like a background colour maybe dark blue with a border.

Target Market(s)

Mining Community

Industry/Entity Type

Mechanical

Requirements
Must have
• Logo colours

```html
<!DOCTYPE html>
<html lang="en">
<head>
<meta charset="utf-8">
<title>KRT Mechanical – Workshop Sign</title>
<link rel="stylesheet" href="https://fonts.googleapis.com/css2?family=Russo+One&display=swap">
<style>
  :root {
    --page: #ffffff;
    --plate-light: #2a3cb8;
    --plate-mid: #1f2c94;
    --plate-dark: #1a1f66;
    --frame: #d9dde3;
    --frame-shade: #9aa1ab;
    --brand-blue: #1e8ff0;
    --brand-blue-deep: #0b56b8;
    --chrome-light: #f4f4f4;
    --chrome-dark: #8f959c;
    --badge-text: #ffffff;
  }
  html, body {
    margin: 0;
    padding: 0;
    width: 1200px;
    height: 255px;
    overflow: hidden;
    background: var(--page);
  }
  .sign {
    display: block;
    width: 1200px;
    height: 255px;
  }
  .sign-name {
    font-family: "Russo One", "Arial Black", sans-serif;
  }
  .badge-name {
    font-family: "Russo One", "Arial Black", sans-serif;
    fill: var(--badge-text);
  }
</style>
</head>
<body>
<svg class="sign" viewBox="0 0 1200 255" xmlns="http://www.w3.org/2000/svg">
  <defs>
    <radialGradient id="plateGradient" cx="50%" cy="50%" r="70%">
      <stop offset="0%" stop-color="var(--plate-light)"/>
      <stop offset="60%" stop-color="var(--plate-mid)"/>
      <stop offset="100%" stop-color="var(--plate-dark)"/>
    </radialGradient>
    <linearGradient id="frameGradient" x1="0" y1="0" x2="1" y2="0">
      <stop offset="0%" stop-color="var(--frame-shade)"/>
      <stop offset="50%" stop-color="var(--frame)"/>
      <stop offset="100%" stop-color="var(--frame-shade)"/>
    </linearGradient>
    <linearGradient id="blueLetters" x1="0" y1="0" x2="0" y2="1">
      <stop offset="0%" stop-color="var(--brand-blue)"/>
      <stop offset="55%" stop-color="var(--brand-blue)"/>
      <stop offset="56%" stop-color="var(--brand-blue-deep)"/>
      <stop offset="100%" stop-color="var(--brand-blue)"/>
    </linearGradient>
    <linearGradient id="chromeLetters" x1="0" y1="0" x2="0" y2="1">
      <stop offset="0%" stop-color="var(--chrome-light)"/>
      <stop offset="55%" stop-color="var(--chrome-light)"/>
      <stop offset="56%" stop-color="var(--chrome-dark)"/>
      <stop offset="100%" stop-color="var(--chrome-light)"/>
    </linearGradient>
    <filter id="letterShadow" x="-5%" y="-20%" width="110%" height="150%">
      <feDropShadow dx="2" dy="3" stdDeviation="2" flood-color="#000" flood-opacity="0.55"/>
    </filter>
  </defs>

  <!-- Background plate -->
  <rect class="plate" x="50" y="45" width="1107" height="166" fill="url(#plateGradient)"
        role="img" aria-label="Dark blue diamond tread-plate texture"/>

  <!-- Frame -->
  <g class="frame" stroke="url(#frameGradient)" stroke-width="2.5" fill="none">
    <polyline points="178,55 61,55 61,201 907,201"/>
    <polyline points="220,56 1145,56 1145,201 960,201"/>
  </g>
  <g class="frame-accents" stroke="var(--frame)" stroke-width="2.5">
    <line x1="185" y1="61" x2="191" y2="50"/>
    <line x1="193" y1="61" x2="199" y2="50"/>
    <line x1="940" y1="206" x2="946" y2="195"/>
    <line x1="948" y1="206" x2="954" y2="195"/>
  </g>
  <circle class="frame-dot" cx="220" cy="56" r="4.5" fill="var(--frame)"/>
  <circle class="frame-dot" cx="907" cy="201" r="4.5" fill="var(--frame)"/>

  <!-- Business name -->
  <g class="sign-name" filter="url(#letterShadow)">
    <text x="94" y="163" font-size="80" textLength="248" lengthAdjust="spacingAndGlyphs"
          fill="url(#blueLetters)">KRT</text>
    <text x="377" y="163" font-size="80" textLength="516" lengthAdjust="spacingAndGlyphs"
          fill="url(#chromeLetters)">MECHANICAL</text>
  </g>

  <!-- Logo position: name set plainly -->
  <g class="badge">
    <circle cx="1037" cy="130" r="58" fill="none" stroke="var(--frame)" stroke-width="2"/>
    <text class="badge-name" x="1037" y="128" font-size="28" text-anchor="middle">KRT</text>
    <text class="badge-name" x="1037" y="150" font-size="12" text-anchor="middle">MECHANICAL</text>
  </g>
</svg>
</body>
</html>
```